4 x Designs Required

Hi There,
I require 4 x different designs to be made for 4 new brands of mine however they can be quite interchangeable. HR Plinkr and Marketing Plinkr can be similar just with a difference in colour. The same goes for the Bulletin brands. This means there are ultimately two designs that need perfecting.

There must be a click here CTA on the banner somewhere. :-)

I require the banners in 728x90 format and 960x90 please.

Please use strap lines on the banners such as:
Essential Whitepapers for HR Professionals
Essential Whitepapers for Marketing Professionals
Your No.1 Whitepaper Resource

The brand names:
HR Plinkr
Marketing Plinkr
HR Dispatchly
Marketing Dispatchly

Examples attached.

```html
<!DOCTYPE html>
<html lang="en">
<head>
<meta charset="utf-8">
<title>Whitepaper Banners</title>
<link rel="stylesheet" href="https://fonts.googleapis.com/css2?family=Montserrat:wght@600;700;800;900&display=swap">
<style>
  :root {
    --page: #ffffff;
    --speckle: #d6d6d8;
    --ink: #1c1c1c;
    --ink-soft: #2a2020;
    --orange: #e0714a;
    --orange-shade: #b5634f;
    --slate: #4a5a78;
    --sun: #fde100;
    --gold: #e9cf1a;
    --navy: #464e66;
    --amber: #f8a431;
    --amber-light: #fbbd2e;
    --amber-deep: #e0993e;
    --white: #ffffff;
  }
  * { margin: 0; padding: 0; box-sizing: border-box; }
  html, body {
    width: 848px;
    height: 1200px;
    overflow: hidden;
    background: var(--page);
  }
  .sheet {
    position: relative;
    width: 848px;
    height: 1200px;
  }
  .banner {
    position: absolute;
    left: 0;
    width: 848px;
    height: 103.5px;
    display: block;
  }
  .banner--marketing { top: 240px; }
  .banner--dispatch { top: 513px; }
  .banner--plinkr { top: 786px; }
  .banner text { font-family: 'Montserrat', sans-serif; }
  .brand { font-weight: 800; }
  .strap { font-weight: 700; }
  .cta-label { font-weight: 800; }
  .badge-text { font-weight: 900; text-anchor: middle; }
</style>
</head>
<body>
<main class="sheet">

  <!-- Marketing Dispatchly -->
  <svg class="banner banner--marketing" viewBox="0 0 1623 198" preserveAspectRatio="none" aria-label="Marketing Dispatchly banner">
    <rect class="speckle-field" width="1623" height="198" fill="var(--speckle)"/>
    <polygon class="corner-shard" points="0,55 122,45 62,198 0,198" fill="var(--slate)"/>
    <path class="body-pill" d="M247,0 H1623 V198 H247 A99,99 0 0 1 247,0 Z" fill="var(--orange)"/>
    <polygon class="corner-speckle" points="1623,55 1540,150 1623,198" fill="var(--speckle)"/>
    <polygon class="corner-shard" points="1623,85 1545,185 1623,198" fill="var(--slate)"/>
    <circle class="glow-disc" cx="1110" cy="75" r="150" fill="var(--orange-shade)" opacity="0.75"/>
    <circle class="badge-ring" cx="1378" cy="92" r="130" fill="var(--gold)" stroke="var(--ink-soft)" stroke-width="20"/>
    <text class="brand" x="224" y="82" font-size="44" fill="var(--ink)">Marketing Dispatchly</text>
    <text class="strap" x="224" y="148" font-size="25" fill="var(--ink-soft)">Essential Whitepapers for Marketing Professionals</text>
    <g class="cta">
      <rect x="988" y="122" width="200" height="52" rx="26" fill="#3a2a26"/>
      <circle cx="1163" cy="148" r="40" fill="#2e2220"/>
      <circle cx="1163" cy="148" r="11" fill="var(--gold)"/>
      <text class="cta-label" x="998" y="158" font-size="28" fill="var(--gold)">Click Me</text>
    </g>
    <g class="badge-text" font-size="32" fill="var(--ink)">
      <text x="1380" y="65">Your No.1</text>
      <text x="1380" y="103">Whitepaper</text>
      <text x="1382" y="142">Resource</text>
    </g>
  </svg>

  <!-- HR Dispatchly -->
  <svg class="banner banner--dispatch" viewBox="0 0 1623 198" preserveAspectRatio="none" aria-label="HR Dispatchly banner">
    <rect class="speckle-field" width="1623" height="198" fill="var(--speckle)"/>
    <path class="body-pill" d="M210,-10 H1320 V188 H210 A99,99 0 0 1 210,-10 Z" fill="var(--sun)" stroke="var(--ink)" stroke-width="16"/>
    <circle class="badge-ring" cx="1378" cy="88" r="162" fill="var(--ink)"/>
    <circle class="badge-core" cx="1382" cy="88" r="122" fill="var(--sun)"/>
    <text class="brand" x="235" y="75" font-size="46" fill="var(--ink)">HR Dispatchly</text>
    <text class="strap" x="235" y="140" font-size="26" fill="var(--ink)">Essential Whitepapers for HR Professionals</text>
    <g class="cta">
      <rect x="865" y="42" width="250" height="72" rx="36" fill="#262626"/>
      <circle cx="1113" cy="80" r="56" fill="#262626"/>
      <circle cx="1113" cy="80" r="16" fill="var(--sun)"/>
      <text class="cta-label" x="900" y="91" font-size="36" fill="var(--sun)">Click Me</text>
    </g>
    <g class="badge-text" font-size="32" fill="var(--ink)">
      <text x="1382" y="66">Your No.1</text>
      <text x="1380" y="105">Whitepaper</text>
      <text x="1384" y="144">Resource</text>
    </g>
  </svg>

  <!-- HR Plinkr -->
  <svg class="banner banner--plinkr" viewBox="0 0 1623 198" preserveAspectRatio="none" aria-label="HR Plinkr banner">
    <rect class="speckle-field" width="1623" height="198" fill="var(--speckle)"/>
    <rect class="base-strip" x="5" y="178" width="875" height="40" rx="18" fill="var(--amber)"/>
    <path class="body-panel" d="M0,0 H860 Q925,0 925,88 Q925,178 860,178 H0 Z" fill="var(--navy)"/>
    <g class="cta">
      <rect x="624" y="28" width="240" height="58" rx="29" fill="var(--sun)"/>
      <circle cx="827" cy="95" r="68" fill="var(--sun)"/>
      <circle cx="827" cy="98" r="28" fill="#000"/>
      <text class="cta-label" x="653" y="68" font-size="27" fill="var(--ink)">Click Me</text>
    </g>
    <text class="brand" x="85" y="78" font-size="42" fill="var(--white)">HR Plinkr</text>
    <text class="strap" x="85" y="136" font-size="26" fill="#e8e8ee">Essential Whitepapers for HR Professionals</text>
    <path class="side-wedge" d="M1190,0 H1623 V198 H1215 Q1130,100 1160,30 Q1175,0 1190,0 Z" fill="var(--amber)"/>
    <path class="wedge-edge" d="M1215,198 Q1130,100 1160,30 Q1175,0 1190,0" fill="none" stroke="var(--ink)" stroke-width="5"/>
    <polygon class="wedge-flare" points="1190,0 1623,0 1623,25 1500,110" fill="var(--amber-light)"/>
    <circle class="badge-disc" cx="1337" cy="95" r="145" fill="var(--navy)"/>
    <circle class="badge-sun" cx="1383" cy="235" r="70" fill="var(--amber-deep)"/>
    <g class="rise-arrow" fill="none" stroke="#222" stroke-width="3">
      <path d="M1475,198 Q1510,120 1496,30"/>
      <path d="M1482,42 L1496,22 L1506,44" fill="#222"/>
    </g>
    <g class="badge-text" font-size="27" fill="var(--white)" style="font-weight:800">
      <text x="1342" y="63">Your No.1</text>
      <text x="1342" y="96">Whitepaper</text>
      <text x="1344" y="130">Resource</text>
    </g>
  </svg>

</main>
</body>
</html>
```